Morvetta Designs - Online Shoe Shop

Morvetta is an online shoes and bags shop. We sell Imported Genuine Leather shoes and bags our market is LSM 8-10. We mainly sell women shoes and bags and we will also be introducing men’s shoes and belts.
I would like a website design and development that is responsive, clean, elegant and easy to use. Where customers can make a purchase online.
Have CATEGORIES in SHOE STYLE (i.e. Heels, Sandals, Pumps, Mules, Boots, Sneaker, Flats, etc) and PRICE RANGE should be in South African Rands currency, COLOUR, SIZE.
For shoe images we should be able to add videos as well.
Header and Footer Menu should have the basic menu list. Header Menu (New Arrivals, Preorder, Women’s Collection, Men’s Collection, Summer 2020 Collection, Winter 2020 Collection, Bags, Accessories, Sale, etc
Auto display when the item is SOLD OUT. Add an option for a user to get notification on when the item is back in stock.
Icons to show when shoes are on sale and Show was and now price.
Users to be able to review and rate the items.
Discount codes for new email subscribers.
Consumers should be able to pay using different options, Credit card, QuidLane, EFT, etc
Add an option for discount coupons at checkout.
After placing and order they should receive an email with order receipt.
Site should have a shipping and tracking option. International shipping such as KRT and BOLTAIR. For local shipping in South Africa please add Quickpath Couriers and Zenobi Couriers.
Backend: Backend should be easy to add more categories, items and changing header banners, adding sale alerts. To get notification when the stock is low and sold out. Get notification when an order is placed online so to prepare packing for shipping.
Can we make sure that the SEO is in place and bare in mind all searchy rules to avoid being penalized.
Target Market(s)
Women from age 25-65
LSM 8-10
Entire South Africa and neighboring countries
Industry/Entity Type
Shoe Store
Coding
Coded - Design and coding required
Number of Pages Required
5+ page
Requirements
Must have
- Responsive
Clean
Modern
Shopping cart
Shipping options integration
Newsletter subscription
Social media icons
Nice to have
- The business colors are Gold and White or Gold and Black

```html
<!DOCTYPE html>
<html lang="en">
<head>
<meta charset="utf-8">
<title>Morvetta Designs – Online Shoe Shop</title>
<link href="https://fonts.googleapis.com/css2?family=Montserrat:wght@400;500;600;700&family=Lato:wght@400;700;900&family=Tinos&display=swap" rel="stylesheet">
<style>
:root{
  --gold:#c9a633;
  --gold-dark:#b08d57;
  --ink:#111;
  --dark:#222;
  --grey:#666;
  --line:#d9d9d9;
  --card:#f3f3f3;
  --red:#e0262c;
  --orange:#f07a1a;
}
*{margin:0;padding:0;box-sizing:border-box}
html,body{width:1200px;height:4441px;overflow:hidden;background:#fff}
body{position:relative;font-family:"Montserrat",sans-serif;color:var(--ink)}
.abs{position:absolute}
.topbar{left:0;top:0;width:1200px;height:48px;background:var(--dark);color:#fff;font:600 14px "Montserrat",sans-serif;display:flex;align-items:center;justify-content:center}
.util{top:104px;left:76px;display:flex;gap:32px;font:500 12px "Montserrat",sans-serif}
.brand{display:flex;align-items:center;gap:8px;font:700 28px "Montserrat",sans-serif}
.brand i{display:block;width:18px;height:18px;background:var(--ink)}
.header-brand{left:0;width:1200px;top:90px;justify-content:center}
.code{left:731px;top:96px;display:flex;align-items:center;gap:12px;font:500 12px "Montserrat",sans-serif}
.code span{background:var(--gold-dark);color:#fff;padding:9px 9px}
.icons{left:1008px;top:100px;display:flex;gap:20px;align-items:center}
.badge{position:absolute;right:-12px;top:-8px;width:16px;height:16px;border-radius:50%;background:var(--gold);color:#fff;font:700 10px "Lato",sans-serif;display:flex;align-items:center;justify-content:center}
.rule{background:var(--line);height:2px}
.nav{left:80px;top:174px;height:57px;display:flex;align-items:center;gap:31px;font:500 15px "Montserrat",sans-serif}
.hero{left:0;top:231px;width:1200px;height:595px;background:linear-gradient(90deg,#cfcfcf,#ececec 55%,#dcdcdc)}
.hero-photo{left:40px;top:20px;width:540px;height:560px;background:radial-gradient(ellipse at 45% 50%,#6d5f3e,#b9a577 45%,rgba(220,220,220,0) 72%)}
.hero h1{right:93px;top:430px;font:900 60px "Lato",sans-serif;letter-spacing:.5px;white-space:nowrap}
.hero-sub{right:93px;top:503px;font:700 27px "Lato",sans-serif;color:var(--gold-dark)}
.btn-shop{left:950px;top:572px;width:152px;height:45px;background:var(--gold-dark);color:#fff;font:500 17px "Lato",sans-serif;display:flex;align-items:center;justify-content:center}
.tile{display:flex;align-items:flex-end;justify-content:center;color:#fff;font:700 32px "Montserrat",sans-serif;padding-bottom:30px}
.section-title{left:0;width:1200px;text-align:center;font:600 22px "Montserrat",sans-serif}
.card{width:246px;height:373px;background:var(--card);box-shadow:0 1px 4px rgba(0,0,0,.08)}
.card .photo{position:absolute;left:30px;top:36px;width:186px;height:160px;border-radius:10px}
.tag{position:absolute;top:14px;font:13px "Tinos",serif;color:#fff;padding:4px 14px 4px 8px}
.tag.in{left:0;background:var(--gold-dark);clip-path:polygon(0 0,100% 0,84% 50%,100% 100%,0 100%)}
.tag.out{right:0;background:var(--ink);clip-path:polygon(0 0,100% 0,100% 100%,0 100%,12% 50%);padding:4px 8px 4px 16px}
.card .name{position:absolute;left:16px;top:255px;font:500 18px "Montserrat",sans-serif}
.card .price{position:absolute;left:16px;top:284px;font:400 23px "Montserrat",sans-serif;color:var(--gold-dark)}
.card .price s{color:#555;font-size:18px;margin-right:10px}
.card .meta{position:absolute;left:16px;right:16px;top:325px;display:flex;justify-content:space-between;font:12px "Tinos",serif;color:#444}
.card .sizes{position:absolute;left:16px;top:347px;font:11px "Montserrat",sans-serif;letter-spacing:5px}
.dots{position:absolute;right:16px;top:349px;display:flex;gap:3px}
.dots b{width:8px;height:8px;border-radius:50%;display:block}
.hover-icons{position:absolute;left:67px;top:60px;width:112px;height:112px}
.hover-icons b{position:absolute;width:44px;height:44px;border-radius:50%}
.arrow{width:52px;height:52px;border-radius:50%;background:#fff;box-shadow:0 1px 6px rgba(0,0,0,.18);display:flex;align-items:center;justify-content:center}
.cat{display:flex;align-items:center;justify-content:center;color:#fff;font:700 28px "Montserrat",sans-serif}
.promo-left{left:0;top:3246px;width:593px;height:538px;background:linear-gradient(160deg,#efe6d7,#d9c8ad 60%,#c8b496)}
.promo-right{left:593px;top:3246px;width:607px;height:538px;background:var(--gold)}
.field{left:664px;width:448px;height:48px;background:#fff;font:14px "Tinos",serif;color:#666;padding-left:20px;display:flex;align-items:center}
.ship-title{font:600 22px "Montserrat",sans-serif;text-align:center}
.carrier{font:700 40px "Montserrat",sans-serif;letter-spacing:-1px}
.footer{left:0;top:4079px;width:1200px;height:362px;background:var(--dark);color:#fff}
.footer h4{position:absolute;font:600 13px "Montserrat",sans-serif}
.footer p,.footer li{font:400 13px "Montserrat",sans-serif;line-height:32px;list-style:none}
.pay{display:flex;gap:8px}
.pay span{width:50px;height:28px;background:#f2f2f2;color:#334;border-radius:3px;font:600 8px "Montserrat",sans-serif;display:flex;align-items:center;justify-content:center}
</style>
</head>
<body>

<div class="abs topbar">Free Shipping Order Over ZAR250 within Uk</div>

<nav class="abs util"><span>ABOUT US</span><span>BLOG</span><span>CONTACT US</span><span>TRACK ORDER</span></nav>
<div class="abs brand header-brand"><i></i>Morvetta</div>
<div class="abs code">USE DISCOUNT CODE <span>MORVETTA50</span></div>
<div class="abs icons">
  <svg width="18" height="18" viewBox="0 0 18 18"><circle cx="7.5" cy="7.5" r="5.5" fill="none" stroke="#222" stroke-width="2.2"/><line x1="11.5" y1="11.5" x2="16.5" y2="16.5" stroke="#222" stroke-width="2.4"/></svg>
  <svg width="16" height="18" viewBox="0 0 16 18"><circle cx="8" cy="5" r="4.5" fill="#222"/><path d="M0 18c0-6 3-8 8-8s8 2 8 8z" fill="#222"/></svg>
  <div style="position:relative"><svg width="20" height="18" viewBox="0 0 20 18"><path d="M0 1h4l3 10h10l2-7H6" fill="none" stroke="#222" stroke-width="2.2"/><circle cx="8" cy="15" r="2" fill="#222"/><circle cx="16" cy="15" r="2" fill="#222"/></svg><span class="badge">0</span></div>
</div>
<div class="abs rule" style="left:0;top:174px;width:1200px"></div>
<nav class="abs nav">
  <span>New Arrivals</span><span>Preorder</span><span>Women’s Collection</span><span>Men’s Collection</span><span>2020 Collections &#8964;</span><span>Shoes &#8964;</span><span>Bags</span><span>Accessories</span><span>Sale</span>
</nav>
<div class="abs rule" style="left:0;top:230px;width:1200px;height:1px"></div>

<section class="abs hero">
  <div class="abs hero-photo" role="img" aria-label="Snakeskin block-heel pumps on a clear display stand"></div>
  <div class="abs" style="left:0;top:390px;width:1200px;height:2px;background:#9a9a9a"></div>
  <svg class="abs" style="left:1136px;top:250px" width="20" height="34" viewBox="0 0 20 34"><path d="M3 2l14 15L3 32" fill="none" stroke="#fff" stroke-width="2.5"/></svg>
</section>
<h1 class="abs hero" style="background:none;width:auto;height:auto;left:auto;right:93px;top:430px;font:900 60px 'Lato',sans-serif">MORVETTA DESIGNS</h1>
<div class="abs hero-sub">Mauris quis sapien in libero vestibulum.</div>
<div class="abs btn-shop">Shop Now</div>

<div class="abs tile" role="img" aria-label="Woman in a red coat holding a red handbag" style="left:74px;top:891px;width:514px;height:402px;background:linear-gradient(135deg,#d9d4cf,#b31e26 45%,#8aa0bd)">WOMENS</div>
<div class="abs tile" role="img" aria-label="Man in a suit walking up stone stairs" style="left:612px;top:891px;width:514px;height:402px;background:linear-gradient(160deg,#3d4656,#2a303b 60%,#48505c);color:rgba(255,255,255,.45)">MENS</div>
<div class="abs" style="left:612px;top:1055px;width:514px;text-align:center;font:700 56px 'Montserrat',sans-serif;color:rgba(255,255,255,.55)">Coming Soon</div>

<div class="abs rule" style="left:74px;top:1355px;width:1052px;height:1px"></div>
<h2 class="abs section-title" style="top:1414px">NEW ARRIVALS</h2>

<!-- New arrivals -->
<div class="abs card" style="left:78px;top:1484px"><div class="photo" role="img" aria-label="Red stiletto pumps" style="background:radial-gradient(circle,#d7262e 0,#e8a0a2 45%,var(--card) 70%)"></div><span class="tag in">In stock</span><div class="name">Product Name</div><div class="price"><s>R150</s>R100</div><div class="meta"><span>Select Size</span><span>Choose Color</span></div><div class="sizes">S M L</div><div class="dots"><b style="background:var(--gold)"></b><b style="background:#111"></b><b style="background:var(--red)"></b><b style="background:var(--orange)"></b></div></div>
<div class="abs card" style="left:347px;top:1484px"><div class="photo" role="img" aria-label="Pink leather handbag" style="background:radial-gradient(circle,#e46d74 0,#f0b2b5 45%,var(--card) 70%)"></div><div class="hover-icons"><b style="left:0;top:0;background:var(--gold-dark)"></b><b style="left:60px;top:0;background:#111"></b><b style="left:0;top:60px;background:#111"></b><b style="left:60px;top:60px;background:var(--gold-dark)"></b></div><span class="tag in">In stock</span><div class="name">Product Name</div><div class="price"><s>R150</s>R100</div><div class="meta"><span>Select Size</span><span>Choose Color</span></div><div class="sizes">S M L</div><div class="dots"><b style="background:var(--gold)"></b><b style="background:#111"></b><b style="background:var(--red)"></b><b style="background:var(--orange)"></b></div></div>
<div class="abs card" style="left:615px;top:1484px"><div class="photo" role="img" aria-label="Blue running sneakers" style="background:radial-gradient(circle,#2448b8 0,#9fb0e0 45%,var(--card) 70%)"></div><span class="tag out">Sold Out</span><div class="name">Product Name</div><div class="price"><s>R150</s>R100</div><div class="meta"><span>Select Size</span><span>Choose Color</span></div><div class="sizes">S M L</div><div class="dots"><b style="background:var(--gold)"></b><b style="background:#111"></b><b style="background:var(--red)"></b><b style="background:var(--orange)"></b></div></div>
<div class="abs card" style="left:884px;top:1484px"><div class="photo" role="img" aria-label="Brown leather tote bag" style="background:radial-gradient(circle,#8a3c22 0,#c79a88 45%,var(--card) 70%)"></div><div class="name">Product Name</div><div class="price"><s>R150</s>R100</div><div class="meta"><span>Select Size</span><span>Choose Color</span></div><div class="sizes">S M L</div><div class="dots"><b style="background:var(--gold)"></b><b style="background:#111"></b><b style="background:var(--red)"></b><b style="background:var(--orange)"></b></div></div>
<div class="abs arrow" style="left:50px;top:1643px"><svg width="10" height="14" viewBox="0 0 10 14"><path d="M8 1L2 7l6 6" fill="none" stroke="#444" stroke-width="1.6"/></svg></div>
<div class="abs arrow" style="left:1098px;top:1643px"><svg width="10" height="14" viewBox="0 0 10 14"><path d="M2 1l6 6-6 6" fill="none" stroke="#444" stroke-width="1.6"/></svg></div>

<div class="abs rule" style="left:74px;top:1929px;width:1052px;height:1px"></div>
<h2 class="abs section-title" style="top:1990px;font-size:44px">Categories In Shoe Style</h2>

<div class="abs cat" role="img" aria-label="Woman in red heels with black bag" style="left:0;top:2072px;width:395px;height:295px;background:linear-gradient(120deg,#6e6a66,#9a2a2e 50%,#5a5652)">HEELS</div>
<div class="abs cat" role="img" aria-label="Feet in sandals on a street" style="left:395px;top:2072px;width:410px;height:295px;background:linear-gradient(160deg,#b48a5c,#8c7561 50%,#a39a8e)">SANDALS</div>
<div class="abs cat" role="img" aria-label="Navy pumps on a bench" style="left:805px;top:2072px;width:395px;height:295px;background:linear-gradient(160deg,#4a4f58,#6e6e6e 60%,#3b3e46)">PUMPS</div>
<div class="abs cat" role="img" aria-label="Pink bow mules" style="left:0;top:2367px;width:292px;height:295px;background:linear-gradient(160deg,#a88662,#b78f76 50%,#8a7058)">MULES</div>
<div class="abs cat" role="img" aria-label="Black ankle boots" style="left:292px;top:2367px;width:308px;height:295px;background:linear-gradient(160deg,#3a3a3a,#555 50%,#2a2a2a)">BOOTS</div>
<div class="abs cat" role="img" aria-label="Black canvas sneaker" style="left:600px;top:2367px;width:310px;height:295px;background:radial-gradient(circle,#4a4a4a,#0d0d0d 70%)">SNEAKER</div>
<div class="abs cat" role="img" aria-label="Red flats on stone steps" style="left:910px;top:2367px;width:290px;height:295px;background:linear-gradient(160deg,#4e5a6e,#7a7d84 55%,#8a3034)">FLATS</div>

<h2 class="abs section-title" style="top:2730px">BEST SELLER</h2>

<div class="abs card" style="left:78px;top:2801px"><div class="photo" role="img" aria-label="Red stiletto pumps" style="background:radial-gradient(circle,#d7262e 0,#e8a0a2 45%,var(--card) 70%)"></div><span class="tag in">In stock</span><div class="name">Product Name</div><div class="price"><s>R150</s>R100</div><div class="meta"><span>Select Size</span><span>Choose Color</span></div><div class="sizes">S M L</div><div class="dots"><b style="background:var(--gold)"></b><b style="background:#111"></b><b style="background:var(--red)"></b><b style="background:var(--orange)"></b></div></div>
<div class="abs card" style="left:347px;top:2801px"><div class="photo" role="img" aria-label="Pink leather handbag" style="background:radial-gradient(circle,#e46d74 0,#f0b2b5 45%,var(--card) 70%)"></div><div class="hover-icons"><b style="left:0;top:0;background:var(--gold-dark)"></b><b style="left:60px;top:0;background:#111"></b><b style="left:0;top:60px;background:#111"></b><b style="left:60px;top:60px;background:var(--gold-dark)"></b></div><span class="tag in">In stock</span><div class="name">Product Name</div><div class="price"><s>R150</s>R100</div><div class="meta"><span>Select Size</span><span>Choose Color</span></div><div class="sizes">S M L</div><div class="dots"><b style="background:var(--gold)"></b><b style="background:#111"></b><b style="background:var(--red)"></b><b style="background:var(--orange)"></b></div></div>
<div class="abs card" style="left:615px;top:2801px"><div class="photo" role="img" aria-label="Blue running sneakers" style="background:radial-gradient(circle,#2448b8 0,#9fb0e0 45%,var(--card) 70%)"></div><span class="tag out">Sold Out</span><div class="name">Product Name</div><div class="price"><s>R150</s>R100</div><div class="meta"><span>Select Size</span><span>Choose Color</span></div><div class="sizes">S M L</div><div class="dots"><b style="background:var(--gold)"></b><b style="background:#111"></b><b style="background:var(--red)"></b><b style="background:var(--orange)"></b></div></div>
<div class="abs card" style="left:884px;top:2801px"><div class="photo" role="img" aria-label="Brown leather tote bag" style="background:radial-gradient(circle,#8a3c22 0,#c79a88 45%,var(--card) 70%)"></div><div class="name">Product Name</div><div class="price"><s>R150</s>R100</div><div class="meta"><span>Select Size</span><span>Choose Color</span></div><div class="sizes">S M L</div><div class="dots"><b style="background:var(--gold)"></b><b style="background:#111"></b><b style="background:var(--red)"></b><b style="background:var(--orange)"></b></div></div>
<div class="abs arrow" style="left:50px;top:2960px"><svg width="10" height="14" viewBox="0 0 10 14"><path d="M8 1L2 7l6 6" fill="none" stroke="#444" stroke-width="1.6"/></svg></div>
<div class="abs arrow" style="left:1098px;top:2960px"><svg width="10" height="14" viewBox="0 0 10 14"><path d="M2 1l6 6-6 6" fill="none" stroke="#444" stroke-width="1.6"/></svg></div>

<!-- Promo & newsletter -->
<div class="abs promo-left" role="img" aria-label="Legs in black leggings wearing black stiletto heels"></div>
<div class="abs" style="left:88px;top:3296px;font:600 46px/1.15 'Montserrat',sans-serif">Get <span style="color:var(--gold);font-weight:700">75%</span><br>Offer</div>
<div class="abs" style="left:88px;top:3420px;font:500 23px 'Montserrat',sans-serif">Women Footwear</div>
<div class="abs" style="left:88px;top:3486px;font:600 15px 'Montserrat',sans-serif;text-decoration:underline">Buy Now</div>
<div class="abs promo-right"></div>
<div class="abs" style="left:664px;top:3355px;color:#fff;font:600 46px 'Montserrat',sans-serif;line-height:1.1">Join Our Newsletter<br><span style="font-size:44px">For</span> <span style="font-size:31px">Get Discount codes</span></div>
<div class="abs field" style="top:3494px">User Name</div>
<div class="abs field" style="top:3555px">Email ID</div>
<div class="abs" style="left:664px;top:3617px;width:448px;height:48px;background:var(--ink);color:#fff;font:500 17px 'Montserrat',sans-serif;display:flex;align-items:center;justify-content:center">Join Now</div>

<!-- Shipping -->
<div class="abs ship-title" style="left:131px;top:3866px;width:400px">INTERNATIONAL SHIPPING</div>
<div class="abs ship-title" style="left:669px;top:3866px;width:400px">LOCAL SHIPPING</div>
<div class="abs carrier" style="left:100px;top:3924px;color:#d40511">KRT</div>
<div class="abs carrier" style="left:366px;top:3924px;color:#4d148c">BOLTAIR</div>
<div class="abs carrier" style="left:684px;top:3924px;color:#1c3f94;font-size:34px">Quickpath</div>
<div class="abs carrier" style="left:893px;top:3924px;color:#d7282f;font-size:34px">Zenobi</div>

<!-- Footer -->
<footer class="abs footer">
  <h4 style="left:74px;top:44px">CONTACT US</h4>
  <p class="abs" style="left:74px;top:68px;line-height:23px">Any questions? Let us know in store at<br>42 Harbour Lane, or call us on <span style="color:var(--gold)">1800 555 014.</span></p>
  <div class="abs brand" style="left:74px;top:160px;color:#fff;font-size:24px"><i style="background:#fff"></i>Morvetta</div>
  <h4 style="left:460px;top:44px">QUICK LINKS</h4>
  <ul class="abs" style="left:460px;top:68px"><li>New Arrivals</li><li>Preorder</li><li>Women’s Collection</li><li>Men’s Collection</li><li>Summer 2020 Collection</li></ul>
  <ul class="abs" style="left:676px;top:68px"><li>Winter 2020 Collection</li><li>Bags</li><li>Accessories</li><li>Sale</li></ul>
  <h4 style="left:922px;top:44px">SOCIAL NETWORKS</h4>
  <div class="abs" style="left:922px;top:82px;display:flex;gap:12px;font:500 12px 'Montserrat',sans-serif"><span>Facet</span><span>Chirpa</span><span>Snapla</span><span>Pinvale</span></div>
  <div class="abs" style="left:74px;top:261px;width:1052px;height:1px;background:#444"></div>
  <p class="abs" style="left:74px;top:294px;font-size:12px;line-height:16px">Copyright © 2020. Company Name. All Right Reserved</p>
  <div class="abs pay" style="left:791px;top:292px"><span>Cardora</span><span>Ringpay</span><span>Amvale</span><span>QuidLane</span><span>Dinwell</span><span>Findly</span></div>
</footer>

</body>
</html>
```